User Interface Designer Needed

I need a few designs for a property law comparison website. We assist the public with finding a solicitor for the purchase or sale of their house and units. We are currently in the process of creating a questionnaire based woo commerce product filter using gravity forms. I'd like to see designs that use the logo colours. Users will be selecting options such as "Buying" or "Selling", they will then be selecting options such as "House" "Unit" or "Land". Details attached. The final design should communicate ease and simplicity. Questions will be answered one at a time, and the next question is dependent on the answer to the question prior

Target Market(s)

First home buyers, people from ages 18-80 make and female looking to get rid of the hassle of ringing around and going from website to website trying to get a quote

Industry/Entity Type

Real Estate

Number of Pages Required

1 page

Colors
33a6d7

Requirements
Must have
• A design for every question
Nice to have
• Simple symbols or simplistic pictures incorporated, even better if you can turn the question into a picture instead of words eg. A picture of a house, a picture of a unit and a picture of land instead of written answers

```html
<!DOCTYPE html>
<html lang="en">
<head>
<meta charset="utf-8">
<title>Nestwell – Property type</title>
<link rel="stylesheet" href="https://fonts.googleapis.com/css2?family=Roboto:wght@400;500;700&display=swap">
<style>
  :root {
    --brand-blue: #33a6d7;
    --text-grey: #5a5a5a;
    --rule-grey: #555555;
    --card-bg: #f1f1f1;
    --card-border: #d6d6d6;
    --selected-green: #3aa63a;
    --hover-green: #a9d6a9;
    --pill-bg: #f5f7f9;
    --button-bg: #3d4e6b;
    --white: #ffffff;
    --icon-ring: #e2e2e2;
  }
  * { box-sizing: border-box; margin: 0; padding: 0; }
  html, body {
    width: 933px; height: 1200px; overflow: hidden;
    background: var(--white);
    font-family: "Roboto", Arial, sans-serif;
  }
  .site-header {
    position: absolute; left: 0; top: 0; width: 933px; height: 87px;
    border-bottom: 2px solid var(--rule-grey);
  }
  .brand {
    position: absolute; left: 41px; top: 28px;
    display: flex; align-items: center; gap: 8px;
    font-size: 30px; font-weight: 500; color: var(--brand-blue);
    letter-spacing: -0.5px;
  }
  .brand-dot {
    width: 30px; height: 30px; border-radius: 50%;
    border: 4px solid var(--brand-blue);
  }
  .question-pill {
    position: absolute; left: 56px; top: 162px; width: 821px; height: 50px;
    border: 1px solid var(--brand-blue); border-radius: 25px;
  }
  .question-label {
    position: absolute; left: -1px; top: -1px; width: 173px; height: 50px;
    background: var(--pill-bg); border: 1px solid #d8dde2; border-radius: 25px;
    padding-left: 21px; line-height: 48px;
    font-size: 16px; color: var(--text-grey);
  }
  .question-label .answer { color: var(--brand-blue); }
  .option-card {
    position: absolute; top: 229px; width: 187px; height: 187px;
    background: var(--card-bg); border: 1px solid var(--card-border);
  }
  .option-card.is-selected { border: 2px solid var(--selected-green); box-shadow: 0 1px 2px rgba(0,0,0,0.15); }
  .option-card.is-hover { border-color: var(--hover-green); }
  .option-icon {
    position: absolute; left: 50%; top: 35px; width: 84px; height: 84px;
    margin-left: -42px; border-radius: 50%;
    border: 2px solid #d4d4d4; box-shadow: 0 1px 2px rgba(0,0,0,0.15);
  }
  .icon-house { background: radial-gradient(circle at 50% 60%, #a8dcc8 0 30%, #f2a08c 31% 40%, var(--icon-ring) 41%); }
  .icon-unit { background: radial-gradient(circle at 50% 50%, #f2a08c 0 22%, #c06b2c 23% 38%, var(--icon-ring) 39%); }
  .icon-land { background: radial-gradient(circle at 50% 55%, #f29a86 0 36%, var(--icon-ring) 37%); }
  .icon-package { background: radial-gradient(circle at 50% 55%, #c06b2c 0 24%, #a8dcc8 25% 38%, var(--icon-ring) 39%); }
  .option-name {
    position: absolute; left: 0; right: 0; top: 133px;
    text-align: center; font-size: 16px; color: var(--text-grey);
  }
  .option-name.is-multiline { text-align: left; left: 37px; top: 133px; line-height: 17px; }
  .save-button {
    position: absolute; left: 693px; top: 447px; width: 183px; height: 35px;
    background: var(--button-bg); color: var(--white); border: 0; border-radius: 2px;
    font-family: "Roboto", Arial, sans-serif; font-size: 15px; font-weight: 700;
    padding-left: 18px; text-align: left;
  }
  .save-button svg { position: absolute; right: 10px; top: 11px; }
</style>
</head>
<body>
  <header class="site-header">
    <div class="brand"><span class="brand-dot"></span>Nestwell.com.au</div>
  </header>

  <main>
    <div class="question-pill">
      <div class="question-label">I am <span class="answer">buying</span></div>
    </div>

    <div class="option-card is-selected" style="left:56px">
      <div class="option-icon icon-house" role="img" aria-label="House icon"></div>
      <div class="option-name">House</div>
    </div>
    <div class="option-card" style="left:268px">
      <div class="option-icon icon-unit" role="img" aria-label="Unit building icon"></div>
      <div class="option-name">Unit</div>
    </div>
    <div class="option-card is-hover" style="left:480px">
      <div class="option-icon icon-land" role="img" aria-label="Land icon"></div>
      <div class="option-name">Land</div>
    </div>
    <div class="option-card" style="left:690px">
      <div class="option-icon icon-package" role="img" aria-label="House and land package icon"></div>
      <div class="option-name is-multiline">House and land<br>package</div>
    </div>

    <button class="save-button" type="button">Save and continue
      <svg width="9" height="14" viewBox="0 0 9 14" aria-hidden="true"><path d="M1.5 1.5 L7 7 L1.5 12.5" fill="none" stroke="#ffffff" stroke-width="1.6"/></svg>
    </button>
  </main>
</body>
</html>
```